Business Card Design Project

Hello,

I am job searching in Canada and need a professional / nice looking business card to give away in networking meetings and informational interviews.

I have extensive market development and business growth experience with strong marketing and project management background.

You'll find specific information about my profile at: http://ca.brindlework.net/in/tomasferrerprofile/

My objective is to work for canadian companies trying to expand their business to Latin America or Hispanic market; or for foreign companies trying to introduce their business to Canada.

Thanks for your help.

Tomas Ferrer

Target Market(s)

Canadian companies trying to expand their business to Latin America or Hispanic market; foreign companies trying to introduce their business to Canada

Industry/Entity Type

Marketing

Requirements
Must have
• The Business card must be two sided, one side must be white, and the other color may be any of the following (or similar):
Green - PMS 349C
Dark Green - PMS 3435
Teal - PMS 315C
Bright Blue - PMS 285C
Earth Brown - PMS 438C
Neutral Gray - PMS 423C
Charcoal Gray - PMS 425C
Silver (metallic) - PMS 877C

Spot UV will be used in the front side to illuminate words or designs so that they reflect and gleam in the light, giving the card a multi-textured look and feel.
Nice to have
• I have attached a QR Code sample as an option to have somewhere in the business card to link it to my Brindlework account instead of having written the long Brindlework address.

It is not a requirement to have it, however, just in case you think is a good idea to have it on the business card.

```html
<!DOCTYPE html>
<html lang="en">
<head>
<meta charset="utf-8">
<title>Tomas Ferrer — Business Card</title>
<link href="https://fonts.googleapis.com/css2?family=Jost:ital,wght@0,300;0,400;1,300&display=swap" rel="stylesheet">
<style>
  :root {
    --page: #ffffff;
    --card: #ffffff;
    --navy: #0b176e;
    --ink: #16181d;
    --rule: #2a45b8;
    --rule-dark: #1b1f2e;
  }
  * { box-sizing: border-box; margin: 0; padding: 0; }
  html, body {
    width: 1200px; height: 1000px; overflow: hidden;
    background: var(--page);
    font-family: "Jost", "Futura", sans-serif;
    color: var(--ink);
  }
  .card {
    position: absolute; left: 76px; top: 200px;
    width: 1050px; height: 600px;
    background: var(--card);
  }
  .mark-placeholder {
    position: absolute; left: 454px; top: 52px;
    width: 130px; height: 130px; border-radius: 50%;
    background: var(--navy);
  }
  .name {
    position: absolute; left: 0; width: 100%; top: 214px;
    text-align: center; font-weight: 400; font-size: 46px;
    letter-spacing: 6px; line-height: 1;
  }
  .title {
    position: absolute; left: 0; width: 100%; top: 274px;
    text-align: center; font-weight: 300; font-style: italic;
    font-size: 30px; letter-spacing: 6px; line-height: 1;
  }
  .contact {
    position: absolute; left: 84px; top: 341px; width: 872px;
  }
  .row {
    position: relative; height: 65px;
    border-top: 1px solid var(--rule);
  }
  .row:last-child { border-bottom: 1px solid var(--rule-dark); height: 66px; }
  .label {
    position: absolute; top: 0; height: 65px; line-height: 67px;
    font-size: 30px; font-weight: 400;
    transform: scaleX(0.72); transform-origin: left;
  }
  .value {
    position: absolute; top: 0; height: 65px; line-height: 65px;
    font-size: 33px; font-weight: 300; letter-spacing: 4.5px;
    white-space: nowrap;
  }
  .divider {
    position: absolute; left: 40px; top: 0; width: 1px;
    height: 196px; background: var(--rule);
  }
  .divider.short { left: 498px; height: 65px; }
  .right { right: 0; text-align: right; }
</style>
</head>
<body>
  <main class="card">
    <div class="mark-placeholder" role="img" aria-label="Monogram mark placeholder"></div>
    <h1 class="name">TOMAS FERRER</h1>
    <p class="title">TITLE HERE</p>

    <section class="contact">
      <div class="divider"></div>
      <div class="row">
        <span class="label" style="left:0">P:</span>
        <span class="value" style="left:88px">604.555.0182</span>
        <span class="label" style="left:460px">T:</span>
        <div class="divider short"></div>
        <span class="value right">@tomasvancity</span>
      </div>
      <div class="row">
        <span class="label" style="left:0">E:</span>
        <span class="value right">tomas@tomasferrer.ca</span>
      </div>
      <div class="row">
        <span class="label" style="left:0">W:</span>
        <span class="value right">brindlework.net/in/tomasferrerprofile</span>
      </div>
    </section>
  </main>
</body>
</html>
```